Marijuana Lifestyle Multi-Shop Brand Website

We need a website that provides an online retail shop for our products, along with the additional functionality:

Main Page: Slider with great photography (we are still looking for a professional photographer to take photos for us.

Shop Tab: E-commerce site.
- Main Categories:
- Accessories
- Bubblers
- Dry Pieces
- Scientific Glass
- Water Pipes
- Custom Shop
- University Store

Stores/Resellers: This is a store look-up, so people can enter their zipcode and find our resellers and partners.

Brand Partners: Just a basic filter and page so that we can highlight our partners and why we've selected them.

Contact Us: Basic Form
- Career Page: Basic Page

About Us: Basic Page

Blog:

Search Bar:

Essentially, we want a near exact copy of this website, but with our brand, logo and content. https://corkwillowbins.com/

This site is really really simple, but we like simple.

Our reserved domain address is: www.runbaketend.com

About Us:
We are multi-shop for marijuana-related accessories. We sell quality glass pipes, vaporizers, amazing storage options, dime bags, custom t-shirts and other stuff.

We have a network of resellers that allow us to put in micro-installations into gift shops, convenience stores, tobacco stores, etc. and we are trying to change the overall perception that buying these items should be mainstream and as transparent as going to the Fen or the Walnut Shop.

I've attached a logo that should give you an idea of our color scheme. We don't have our photography yet for the slider
Updates

As an FYI, for the e-commerce part of my website, I already have a license for WP SwiftTill.

Industry/Entity Type

Shop

```html
<!DOCTYPE html>
<html lang="en">
<head>
<meta charset="utf-8">
<title>verdanest — Home</title>
<link rel="stylesheet" href="https://fonts.googleapis.com/css2?family=Dosis:wght@500&family=Open+Sans:wght@400;600&display=swap">
<style>
  :root {
    --black: #000000;
    --header-bg: #0c0c0c;
    --white: #ffffff;
    --muted: #d8d8d8;
    --lime: #b9cf3c;
    --logo-green: #6f8f1d;
    --rule-grey: #5a5a5a;
    --hero-top: #6b6a66;
    --hero-mid: #4a4541;
    --hero-low: #2a2826;
    --social-1: #3b5ca0;
    --social-2: #cb2027;
    --social-3: #2ba6de;
    --social-4: #3f729b;
  }
  * { margin: 0; padding: 0; box-sizing: border-box; }
  html, body { width: 1200px; height: 752px; overflow: hidden; background: var(--black); }
  body { position: relative; font-family: "Open Sans", Arial, sans-serif; color: var(--white); }

  .site-header {
    position: absolute; left: 0; top: 0; width: 1200px; height: 76px;
    background: repeating-linear-gradient(45deg, #111 0 2px, var(--header-bg) 2px 4px);
  }
  .brand { position: absolute; left: 153px; top: 6px; display: flex; align-items: center; gap: 10px; }
  .brand-mark { width: 62px; height: 62px; border-radius: 50%; background: var(--logo-green); border: 2px solid var(--lime); }
  .brand-name { font-size: 15px; font-weight: 600; color: var(--lime); }
  .main-nav { position: absolute; left: 407px; top: 27px; display: flex; gap: 21px; font-size: 13px; font-weight: 600; }
  .main-nav a { color: var(--white); text-decoration: none; }
  .search { position: absolute; left: 790px; top: 27px; width: 108px; height: 20px; border-bottom: 2px solid var(--white); font-size: 11px; font-weight: 600; padding-left: 2px; }
  .search svg { position: absolute; right: 6px; top: 3px; }
  .phone { position: absolute; left: 927px; top: 27px; display: flex; align-items: center; gap: 10px; font-size: 13px; font-weight: 600; }

  .hero {
    position: absolute; left: 0; top: 76px; width: 1200px; height: 479px;
    background: linear-gradient(180deg, var(--hero-top) 0%, var(--hero-mid) 45%, var(--hero-low) 100%);
  }
  .hero-photo { position: absolute; inset: 0; background: radial-gradient(ellipse 380px 420px at 520px 260px, rgba(30,26,24,.55), transparent 70%), linear-gradient(90deg, rgba(110,80,70,.35), transparent 35%, rgba(150,150,150,.15)); }
  .hero-title { position: absolute; left: 0; width: 1288px; top: 127px; text-align: center; font-family: "Dosis", "Arial Narrow", sans-serif; font-weight: 500; font-size: 37px; letter-spacing: .3px; text-transform: uppercase; }
  .hero-text { position: absolute; left: 383px; width: 520px; top: 180px; text-align: center; font-size: 12.5px; line-height: 18px; }
  .slider-dots { position: absolute; left: 570px; top: 435px; display: flex; gap: 4px; }
  .slider-dots span { width: 12px; height: 12px; border-radius: 50%; border: 1.5px solid var(--white); }
  .slider-dots .is-active { background: var(--white); }

  .site-footer { position: absolute; left: 0; top: 555px; width: 1200px; height: 197px; background: var(--black); }
  .footer-top-rule { position: absolute; left: 502px; top: 23px; width: 196px; height: 2px; background: var(--white); }
  .social { position: absolute; left: 0; width: 1200px; top: 54px; display: flex; justify-content: center; gap: 22px; font-size: 12px; font-weight: 600; }
  .social a { display: flex; align-items: center; gap: 7px; color: var(--white); text-decoration: none; }
  .social i { width: 16px; height: 16px; display: block; }
  .footer-rule { position: absolute; left: 141px; top: 105px; width: 934px; height: 2px; background: linear-gradient(90deg, transparent, var(--rule-grey) 15%, #8a8a8a 50%, var(--rule-grey) 85%, transparent); }
  .category-nav { position: absolute; left: 278px; top: 128px; display: flex; font-size: 12.5px; }
  .category-nav a { color: var(--lime); text-decoration: none; }
  .copyright { position: absolute; left: 0; width: 1133px; top: 161px; text-align: center; font-size: 11px; color: var(--lime); }
</style>
</head>
<body>
  <header class="site-header">
    <a class="brand"><span class="brand-mark"></span><span class="brand-name">verdanest</span></a>
    <nav class="main-nav">
      <a>Stores</a><a>Brand Partners</a><a>Contact Us</a><a>About Us</a><a>Blog</a>
    </nav>
    <div class="search">Search.....
      <svg width="12" height="12" viewBox="0 0 12 12"><circle cx="5" cy="5" r="3.6" fill="none" stroke="#fff" stroke-width="2"/><line x1="7.6" y1="7.6" x2="11" y2="11" stroke="#fff" stroke-width="2.2"/></svg>
    </div>
    <div class="phone">
      <svg width="13" height="17" viewBox="0 0 13 17"><path d="M3 0 L5.5 4 L3.8 5.6 C4.5 8 5.8 10.4 7.6 12 L9.4 10.8 L12.5 14 L10.4 16.6 C5 16 0.5 8 1 1.6 Z" fill="#fff"/></svg>
      <span>+ 00-000-5512-730</span>
    </div>
  </header>

  <section class="hero">
    <div class="hero-photo" role="img" aria-label="Slider photograph: smiling woman in a leather jacket and red scarf holding a black handbag on a city street"></div>
    <h1 class="hero-title">Lorem ipsum dolor set amet dipiscing elit</h1>
    <p class="hero-text">Lorem ipsum dolor sit amet, consectetur adipiscing elit. Duis ut dolor aliquet, aliquet risus quis, ultricies risus. Phasellus luctusrisus id tortor ornare blandit.</p>
    <div class="slider-dots"><span></span><span></span><span></span><span class="is-active"></span><span></span></div>
  </section>

  <footer class="site-footer">
    <div class="footer-top-rule"></div>
    <div class="social">
      <a><i style="background:var(--social-1)"></i>Friendwall</a>
      <a><i style="background:var(--social-2)"></i>Pinboardly</a>
      <a><i style="background:var(--social-3)"></i>Chirpline</a>
      <a><i style="background:var(--social-4)"></i>Snapframe</a>
    </div>
    <div class="footer-rule"></div>
    <nav class="category-nav">
      <a style="margin-right:32px">Accessories</a>
      <a style="margin-right:32px">Bubblers</a>
      <a style="margin-right:21px">Dry Pieces</a>
      <a style="margin-right:25px">Scientific Glass</a>
      <a style="margin-right:25px">Water Pipes</a>
      <a style="margin-right:32px">Custom Shop</a>
      <a>University Store</a>
    </nav>
    <p class="copyright">Copyright © 2008-2014 verdanest. All rights reserved.</p>
  </footer>
</body>
</html>
```